Tallow Bodyweight Gym Website

We need a website design for our gym.

Tallow is the UAE's first calisthenics and parkour gym. The theme under which the gym revolves is that one does not require any machinery to workout as our bodies could be themselves the machinery. The gym is designed to be the more of a social hub rather than an "in-and-out" gym, where people come train, have fun, hang out and socialize for a few hours rather than just train for 60 minutes then leave. The gym is designed to be a big open space with lots of natural sunlight, natural wood and plants all over the place to create a natural and refreshing setting. We also use recycled material throughout the gym and recycle our waste as being green is part of our philosophy. We currently also have some of the world's top and most recognized calisthenics athletes working with us.

We would like our website to reflect all that as well as provide a simple, interactive and fun way for visitors to be able to get class and gym information, check out gym media and contact us for bookings.

Target Market(s)

Ages 15-35

Industry/Entity Type

Fitness

Coding

Coded - Design and coding required

Number of Pages Required

4 page

Font styles to use
Decorative

Colors
0792cd

Requirements
Must have
• Class descriptions
• Gym description
• Class schedules
• Trainer profiles
• Gym philosophy
• Contact Details
Nice to have
• A link to contact us directly for a free first trial class

```html
<!DOCTYPE html>
<html lang="en">
<head>
<meta charset="utf-8">
<title>Tallow Bodyweight Gym</title>
<link href="https://fonts.googleapis.com/css2?family=Ubuntu:ital,wght@0,300;0,400;0,500;0,700;1,400&display=swap" rel="stylesheet">
<style>
:root{
  --blue:#0a93c4;
  --blue-deep:#0885b2;
  --ink:#262324;
  --panel:#2b2829;
  --footer:#333233;
  --line:#4a4748;
  --text:#e9e9e9;
  --muted:#bdbdbd;
  --white:#ffffff;
}
*{box-sizing:border-box;margin:0;padding:0}
html,body{width:810px;height:1200px;overflow:hidden;background:var(--panel)}
body{font-family:"Ubuntu",sans-serif;color:var(--text);position:relative}
.abs{position:absolute}
.hero{left:0;top:0;width:810px;height:417px;background:radial-gradient(ellipse at 70% 40%,#6d6a66 0%,#3f3c3b 45%,#262424 100%)}
.logo{left:40px;top:10px;display:flex;align-items:center;gap:6px;font-weight:700;font-size:22px;color:var(--white)}
.logo-dot{width:9px;height:9px;border-radius:50%;background:var(--blue)}
.nav{left:453px;top:18px;display:flex;align-items:center;font-size:9px;color:var(--white)}
.nav a{color:inherit;text-decoration:none;padding:4px 12px}
.nav a.active{background:var(--blue)}
.nav .sep{opacity:.9}
.headline{left:0;width:810px;top:143px;text-align:center;font-weight:700;font-size:27px;line-height:35px;letter-spacing:-0.4px;color:var(--white)}
.btn-hero{left:339px;top:233px;width:132px;height:32px;background:var(--blue);color:var(--white);font-size:9px;display:flex;align-items:center;justify-content:center}
.dots{left:388px;top:344px;display:flex;gap:5px}
.dots span{width:8px;height:8px;border-radius:50%;background:var(--white)}
.dots span:first-child{background:var(--blue)}
.card{top:366px;width:228px;height:135px;padding:14px 15px}
.card h3{font-size:15px;font-weight:500;color:var(--white);line-height:16px}
.card .sub{font-size:10px;font-style:italic;font-weight:300;color:#d6eef7;text-transform:uppercase}
.card.schedule{left:62px;background:var(--white)}
.card.schedule h3{color:var(--blue)}
.card.schedule .sub{color:#555;text-transform:none;font-size:11px}
.sched{margin-top:12px;font-size:9px;color:#333}
.sched li{list-style:none;display:flex;align-items:center;height:22.5px}
.sched i{width:9px;height:7px;border:1.5px solid var(--blue);border-top-width:3px;margin-right:7px}
.sched .t{position:absolute;left:132px}
.card.member{left:290px;background:var(--blue)}
.card.trainer{left:518px;background:var(--blue-deep)}
.card .body{position:absolute;left:69px;top:58px;width:144px;font-size:8.3px;line-height:11.5px;color:var(--white);text-align:justify}
.card svg{position:absolute;left:15px;top:68px}
.col-divider{left:501px;top:501px;width:2px;height:537px;background:#3a3738}
.sec-title{font-size:15px;font-weight:500;color:var(--white);padding-bottom:2px;border-bottom:2px solid var(--blue);display:inline-block}
.about-photo{left:64px;top:557px;width:214px;height:192px;background:linear-gradient(135deg,#3d4f59,#7f6a53 55%,#2e5e8a)}
.about-text{font-size:8.6px;line-height:13px;letter-spacing:-0.2px;color:var(--text);text-align:justify}
.team-photo{top:867px;width:130px;height:102px;background:linear-gradient(160deg,#b8c2c7,#6f7b80 60%,#4b5a64)}
.team-name{top:977px;width:130px;text-align:center;font-size:11px;font-weight:500;color:var(--white);line-height:12px}
.team-name small{display:block;font-size:6.5px;font-weight:400}
.btn-team{left:70px;top:999px;width:115px;height:27px;border:1px solid var(--white);font-size:9px;display:flex;align-items:center;justify-content:center;color:var(--white)}
.side-title{left:513px;width:233px;font-size:15px;font-weight:500;color:var(--blue);border-bottom:2px solid var(--blue);padding-bottom:1px;display:flex;justify-content:space-between;align-items:center}
.event-photo{left:521px;top:574px;width:89px;height:64px;background:linear-gradient(135deg,#1f6fa3,#c8cdd0 55%,#7e5f3d)}
.event-text{left:618px;top:577px;width:112px;font-size:7.3px;line-height:10px;color:var(--white)}
.event-row{left:513px;width:233px;height:40px;padding:8px 2px;border-bottom:2px solid #4a4748;display:flex;justify-content:space-between;align-items:center}
.event-row b{display:block;font-size:11px;font-weight:500;color:var(--white)}
.event-row small{display:block;font-size:6px;font-style:italic;color:var(--white)}
.event-row.current{background:#3c3a3b;border-bottom:none}
.hr{left:502px;width:308px;height:2px;background:#3a3738}
.tweet{left:515px;width:230px;display:flex;gap:8px}
.avatar{width:43px;height:43px;background:linear-gradient(160deg,#8a6b58,#3a2d28)}
.tweet b{display:block;font-size:11px;font-weight:500;color:var(--white);margin-bottom:2px}
.tweet p{font-size:5.9px;line-height:7px;color:var(--white);width:130px}
.footer{left:0;top:1038px;width:810px;height:128px;background:var(--footer)}
.footer-mark{left:86px;top:1052px;display:flex;align-items:center;gap:6px;font-size:24px;font-weight:700;color:var(--white)}
.footer-mark span{width:13px;height:13px;border-radius:50%;background:var(--white)}
.links{top:1066px;font-size:10.5px;line-height:21.6px;color:#e6e6e6;list-style:none}
.bar{left:0;top:1166px;width:810px;height:34px;background:var(--blue);font-size:8.5px;color:var(--white)}
.bar .copy{position:absolute;left:125px;top:12px}
.bar .copy b{font-weight:700}
.bar .find{position:absolute;left:559px;top:10px;display:flex;align-items:center;gap:10px}
.bar .find i{width:10px;height:10px;border-radius:50%;background:#b9e2f1;display:block}
</style>
</head>
<body>
<div class="abs hero" role="img" aria-label="Photo of an athlete mid-leap in a calisthenics gym, darkened"></div>

<div class="abs logo">Tallow<span class="logo-dot"></span></div>
<nav class="abs nav">
  <a class="active">HOME</a><a>CLASSES</a><span class="sep">|</span><a>ABOUT US</a><span class="sep">|</span><a>GALLERY</a><span class="sep">|</span><a>CONTACT US</a>
</nav>
<h1 class="abs headline">FIND YOUR OWN WAY TO DIFINE<br>YOUR BODY</h1>
<div class="abs btn-hero">VIEW CLASSES</div>
<div class="abs dots"><span></span><span></span><span></span></div>

<section class="abs card schedule">
  <h3>CLASS SCHEDULES</h3>
  <div class="sub">TODAY CLASS</div>
  <ul class="sched">
    <li><i></i>Boxing<span class="t">1:00pm-5pm</span></li>
    <li><i></i>Cardio Fitness<span class="t">5:00pm-8pm</span></li>
    <li><i></i>Yoga<span class="t">6:00am-9:00pm</span></li>
  </ul>
</section>
<section class="abs card member">
  <h3>MEMBERSIP CARDS</h3>
  <div class="sub">25% DISCOUNT FOR ALL MEMBERS</div>
  <svg width="46" height="24" viewBox="0 0 46 24" fill="#fff"><circle cx="23" cy="5" r="5"/><path d="M14 24c0-8 4-12 9-12s9 4 9 12z"/><circle cx="9" cy="8" r="4"/><path d="M1 24c0-7 3-10 8-10 2 0 3 .5 4 1.5-1.5 2.5-2 5-2 8.5z"/><circle cx="37" cy="8" r="4"/><path d="M45 24c0-7-3-10-8-10-2 0-3 .5-4 1.5 1.5 2.5 2 5 2 8.5z"/></svg>
  <p class="body">Lorem ipsum dolor sit amet, consectetur adipiscing elit, sed do eiusmod tempor incididunt ut labore et dolore magna aliqua. Ut enim ad minim veniam,</p>
</section>
<section class="abs card trainer">
  <h3>PERSONAL TRAINING</h3>
  <div class="sub">SIGN UP TODAY</div>
  <svg width="46" height="24" viewBox="0 0 46 24" fill="#fff"><circle cx="23" cy="6" r="6"/><path d="M12 24c0-8 5-11 11-11s11 3 11 11z"/></svg>
  <p class="body">Lorem ipsum dolor sit amet, consectetur adipiscing elit, sed do eiusmod tempor incididunt ut labore et dolore magna aliqua. Ut enim ad minim veniam,</p>
</section>

<div class="abs col-divider"></div>

<h2 class="abs sec-title" style="left:66px;top:520px">ABOUT US</h2>
<div class="abs about-photo" role="img" aria-label="Photo of an athlete on gymnastic rings inside the gym"></div>
<p class="abs about-text" style="left:288px;top:553px;width:204px">Lorem ipsum dolor sit amet, consectetur adipiscing elit, sed do eiusmod tempor incididunt ut labore et dolore magna aliqua. Ut enim ad minim veniam, quis nostrud exercitation ullamco laboris nisi ut aliquip ex ea commodo consequat. Duis aute irure dolor in reprehenderit in voluptate velit esse cillum dolore eu fugiat nulla pariatur. Excepteur sint occaecat cupidatat non proident, sunt in culpa qui officia deserunt mollit anim id est laborum<br><br>Sed ut perspiciatis unde omnis iste natus error sit voluptatem accusantium doloremque laudantium, totam rem aperiam, eaque ipsa quae ab illo inventore veritatis et quasi architecto beatae vitae dicta sunt explicabo.</p>
<p class="abs about-text" style="left:66px;top:760px;width:426px">Lorem ipsum dolor sit amet, consectetur adipiscing elit, sed do eiusmod tempor incididunt ut labore et dolore magna aliqua. Ut enim ad minim veniam, quis nostrud exercitation ullamco laboris nisi ut aliquip ex ea commodo consequat. Duis aute irure dolor in reprehenderit in voluptate velit esse cillum dolore eu fugiat nulla pariatur. Excepteur sint occaecat cupidatat non proident, sunt in culpa qui officia deserunt mollit anim id est laborum.</p>

<h2 class="abs sec-title" style="left:66px;top:832px">TALLOW TEAM</h2>
<div class="abs team-photo" style="left:68px" role="img" aria-label="Portrait of a fitness trainer with a clipboard"></div>
<div class="abs team-photo" style="left:211px" role="img" aria-label="Portrait of a fitness trainer with a clipboard"></div>
<div class="abs team-photo" style="left:355px" role="img" aria-label="Portrait of a fitness trainer with a clipboard"></div>
<div class="abs team-name" style="left:68px">OMAR REYES<small>FITNESS TRAINER</small></div>
<div class="abs team-name" style="left:211px">OMAR REYES<small>FITNESS TRAINER</small></div>
<div class="abs team-name" style="left:355px">OMAR REYES<small>FITNESS TRAINER</small></div>
<div class="abs btn-team">VIEW ALL TEAM</div>

<h2 class="abs side-title" style="top:541px">UPCOMING EVENTS
  <svg width="14" height="8" viewBox="0 0 14 8"><path d="M1 1l6 5 6-5" fill="none" stroke="#0a93c4" stroke-width="2"/></svg></h2>
<div class="abs event-photo" role="img" aria-label="Photo of gymnastic rings hanging in the gym"></div>
<p class="abs event-text">Sed ut perspiciatis unde omnis iste natus error sit voluptatem accusantium doloremque laudantium, totam rem aperiam, eaque ipsa quae ab illo tecto beatae vitacabo.</p>
<div class="abs event-row" style="top:646px"><div><b>INDOOR CYCLING</b><small>STRENGTH, STAMBO, POWER</small></div>
  <svg width="10" height="14" viewBox="0 0 10 14"><path d="M2 1l6 6-6 6" fill="none" stroke="#fff" stroke-width="2"/></svg></div>
<div class="abs event-row" style="top:685px"><div><b>YOGA PILATES</b><small>RELAXATION, MIND REST</small></div>
  <svg width="10" height="14" viewBox="0 0 10 14"><path d="M2 1l6 6-6 6" fill="none" stroke="#fff" stroke-width="2"/></svg></div>
<div class="abs event-row current" style="top:724px"><div><b>BOXING</b><small>STRONG, SHARPER</small></div>
  <svg width="10" height="14" viewBox="0 0 10 14"><path d="M2 1l6 6-6 6" fill="none" stroke="#fff" stroke-width="2"/></svg></div>
<div class="abs hr" style="top:775px"></div>
<h2 class="abs side-title" style="top:786px">TRANING CLASSES
  <svg width="10" height="14" viewBox="0 0 10 14"><path d="M2 1l6 6-6 6" fill="none" stroke="#0a93c4" stroke-width="2"/></svg></h2>
<div class="abs hr" style="top:820px"></div>
<h2 class="abs side-title" style="top:834px">LASTEST TWEETS
  <svg width="14" height="8" viewBox="0 0 14 8"><path d="M1 1l6 5 6-5" fill="none" stroke="#0a93c4" stroke-width="2"/></svg></h2>
<div class="abs tweet" style="top:864px"><div class="avatar" role="img" aria-label="Profile photo"></div><div><b>MIRA HADDAD</b><p>RIGHT @LENFIELD WE NEED POLICIES THAT SUPPORT TEACHING &amp; LEARNING, NOT TEST &amp; PUNIS</p></div></div>
<div class="abs tweet" style="top:917px"><div class="avatar" role="img" aria-label="Profile photo"></div><div><b>MIRA HADDAD</b><p>RIGHT @LENFIELD WE NEED POLICIES THAT SUPPORT TEACHING &amp; LEARNING, NOT TEST &amp; PUNIS</p></div></div>
<div class="abs tweet" style="top:969px"><div class="avatar" role="img" aria-label="Profile photo"></div><div><b>MIRA HADDAD</b><p>RIGHT @LENFIELD WE NEED POLICIES THAT SUPPORT TEACHING &amp; LEARNING, NOT TEST &amp; PUNIS</p></div></div>

<footer>
  <div class="abs footer"></div>
  <div class="abs footer-mark">Tallow<span></span></div>
  <ul class="abs links" style="left:208px"><li>Brand Guidelines</li><li>Jobs</li><li>Chalk at Work</li><li>Support</li></ul>
  <ul class="abs links" style="left:343px"><li>Privacy</li><li>Security</li><li>Terms of Service</li><li>Policies</li></ul>
  <ul class="abs links" style="left:479px"><li>Status</li><li>API</li><li>Integrations</li><li>Apps</li></ul>
  <ul class="abs links" style="left:614px"><li>Podcast</li><li>Blog</li><li>Contact Us</li><li>@Tallow</li></ul>
  <div class="abs bar">
    <div class="copy"><b>TALLOW</b> Copyright all rights reserved 2015</div>
    <div class="find">Find us: <i></i><i></i><i></i><i></i></div>
  </div>
</footer>
</body>
</html>
```